Luxury Ayurvedic Hair Oil logo and package design

We need a logo and package design for our Ayurvedic and natural hair growth oil. Our company, Velmora, is the premier luxury Ayurvedic beauty brand, bringing ancient East-Indian natural and botanic health and beauty products to the US market. Our first major product - Velmora Hair Growth Oil - is a coconut oil based product that was developed by tribes in the Southern State of Kerala that includes ancient herbs like Gooseberry, Indigo, Indian Aloe, Balloon Vine and Brahmi.

The design should be catered to the high-end luxury market (minimal design, minimal text, fonts that invoke a sense of luxury). The primary colors should be deep blue for the packaging and gold for the characters (it's in the name - Velmora). We are looking to sell our products in Brenvale and Tolland Pryce and require packaging that is in line with products sold at these high-end retailers.

The final logo design and packaging should communicate luxury and the ancient wisdom of far-eastern traditions.

Target Market(s)

Velmora's main target is women who value fashionable/quality skincare, beauty, and fragrance products and are open to a medium to high price range. These women love uniqueness in brand and products that cannot be found elsewhere. They are looking for the next new "it" item that will take their haircare and beauty regiment to the next level.

Industry/Entity Type

Hair And Beauty

Font styles to use
Serif

Colors
2f73b3
ffc214

Requirements
Must have
• Must use deep blue (royal blue) background and gold text (to align with brand name). Must use luxurious fonts
Nice to have
• Flowers or other natural symbols, pictures that blend well with the product theme

```html
<!DOCTYPE html>
<html lang="en">
<head>
<meta charset="utf-8">
<title>Velmora Ayurvedic Hair Oil – Label and Carton</title>
<link href="https://fonts.googleapis.com/css2?family=Cinzel:wght@400;500&family=Oswald:wght@300;500&display=swap" rel="stylesheet">
<style>
  :root {
    --navy: #14204f;
    --navy-deep: #101a44;
    --gold: #c9945a;
    --gold-light: #e6b67e;
    --gold-dark: #9c6a38;
    --page: #ffffff;
  }
  html, body {
    margin: 0;
    padding: 0;
    width: 1200px;
    height: 1000px;
    overflow: hidden;
    background: var(--page);
  }
  .canvas {
    position: relative;
    width: 1200px;
    height: 1000px;
  }

  /* ---------- Bottle label (flat) ---------- */
  .bottle-label {
    position: absolute;
    left: 250px;
    top: 473px;
    width: 272px;
    height: 312px;
    background: var(--navy);
    text-align: center;
    color: var(--gold-light);
  }
  .bottle-label .rule {
    position: absolute;
    left: 0;
    right: 0;
    height: 4px;
    background: linear-gradient(90deg, var(--gold-dark), var(--gold-light), var(--gold-dark));
  }
  .bottle-label .rule--top { top: 10px; }
  .bottle-label .rule--bottom { top: 298px; }
  .bottle-label .brand-name {
    position: absolute;
    top: 80px;
    left: 0; right: 0;
    font-family: "Cinzel", serif;
    font-weight: 400;
    font-size: 27px;
    line-height: 27px;
    letter-spacing: 1px;
    color: var(--gold-light);
  }
  .bottle-label .product-name {
    position: absolute;
    top: 168px;
    left: 0; right: 0;
    font-family: "Cinzel", serif;
    font-size: 21px;
    line-height: 27px;
    color: var(--gold);
  }
  .bottle-label .benefits {
    position: absolute;
    top: 234px;
    left: 0; right: 0;
    font-family: "Oswald", sans-serif;
    font-weight: 300;
    font-size: 14px;
    line-height: 22px;
    letter-spacing: 0.3px;
    color: var(--gold);
    text-transform: uppercase;
  }
  .bottle-label .volume {
    position: absolute;
    top: 282px;
    left: 0; right: 0;
    font-family: "Oswald", sans-serif;
    font-weight: 500;
    font-size: 13px;
    line-height: 13px;
    color: var(--gold-light);
  }

  /* ---------- Carton front ---------- */
  .carton {
    position: absolute;
    left: 545px;
    top: 88px;
    width: 356px;
    height: 853px;
    background: var(--navy-deep);
    text-align: center;
  }
  .carton .frame {
    position: absolute;
    inset: 12px;
    border: 4px solid var(--gold);
    box-shadow: inset 0 0 0 1px var(--gold-dark);
  }
  .carton .brand-name {
    position: absolute;
    top: 212px;
    left: 0; right: 0;
    font-family: "Cinzel", serif;
    font-weight: 400;
    font-size: 36px;
    letter-spacing: 1px;
    color: var(--gold-light);
  }
  .carton .product-name {
    position: absolute;
    top: 384px;
    left: 0; right: 0;
    font-family: "Cinzel", serif;
    font-size: 33px;
    line-height: 40px;
    letter-spacing: 1px;
    color: var(--gold);
  }
  .carton .benefits {
    position: absolute;
    top: 527px;
    left: 0; right: 0;
    font-family: "Oswald", sans-serif;
    font-weight: 300;
    font-size: 25px;
    line-height: 42px;
    color: var(--gold);
    text-transform: uppercase;
  }
  .carton .volume {
    position: absolute;
    top: 765px;
    left: 0; right: 0;
    font-family: "Oswald", sans-serif;
    font-weight: 500;
    font-size: 21px;
    color: var(--gold-light);
  }
</style>
</head>
<body>
<main class="canvas">

  <section class="bottle-label">
    <div class="rule rule--top"></div>
    <div class="brand-name">VELMORA</div>
    <div class="product-name">Ayurvedic<br>Hair Oil</div>
    <div class="benefits">Hair growth shoothing<br>moisture healthy hair</div>
    <div class="volume">2 FL. OZ</div>
    <div class="rule rule--bottom"></div>
  </section>

  <section class="carton">
    <div class="frame"></div>
    <div class="brand-name">VELMORA</div>
    <div class="product-name">Ayurvedic<br>Hair Oil</div>
    <div class="benefits">Hair growth<br>Shoothing moisture<br>Healthy hair</div>
    <div class="volume">2 FL. OZ</div>
  </section>

</main>
</body>
</html>
```